The Brightwater Compass Business Card

We need an attractive business card with the logo that we bought from ArtVantly last year.
Our mission is to contribute to change the way today's leaders manage business companies bringing value to the workplace and helping them to build a new model of creating wealth.
Our logo is clear about our values : we seek Positive Change through People and are convinced that the pursuit of individual well-being and the chase of economic results can converge with the right management.
Management Consulting
Corinne Fabrelle
+34 612 98 70 31
corinne.fabrelle@thebrightwatercompass-mail.net
www.thebrightwatercompass-mail.net

```html
<!DOCTYPE html>
<html lang="en">
<head>
<meta charset="utf-8">
<title>The Brightwater Compass – Business Card</title>
<link rel="stylesheet" href="https://fonts.googleapis.com/css2?family=Cormorant+SC:wght@600&family=PT+Sans:wght@400&display=swap">
<style>
  :root {
    --teal: #0f837c;
    --paper: #ffffff;
    --backdrop: #e9e6e2;
    --ink: #2c2c2c;
    --shadow: rgba(0,0,0,0.18);
  }
  * { margin: 0; padding: 0; box-sizing: border-box; }
  html, body { width: 1200px; height: 987px; overflow: hidden; }
  body { background: var(--backdrop); position: relative; font-family: "PT Sans", sans-serif; }

  .card {
    position: absolute;
    left: 293px;
    width: 615px;
    height: 351px;
    box-shadow: 0 2px 6px var(--shadow);
  }
  .card--front { top: 130px; background: var(--paper); text-align: center; }
  .card--back { top: 506px; background: var(--teal); text-align: center; }

  .brand { display: flex; flex-direction: column; align-items: center; }
  .brand__dot { width: 22px; height: 22px; border-radius: 50%; background: var(--teal); }
  .brand__name {
    font-family: "Cormorant SC", serif;
    font-weight: 600;
    color: var(--teal);
    letter-spacing: 0.5px;
  }
  .card--front .brand { padding-top: 58px; gap: 14px; }
  .card--front .brand__name { font-size: 34px; line-height: 1; }

  .holder {
    margin-top: 38px;
    font-family: "Cormorant SC", serif;
    font-weight: 600;
    font-size: 27px;
    color: var(--teal);
    letter-spacing: 0.5px;
  }

  .contacts { list-style: none; margin-top: 20px; }
  .contacts li {
    display: flex; justify-content: center; align-items: center; gap: 6px;
    font-size: 16px; line-height: 24px; color: var(--ink);
  }
  .contacts svg { width: 14px; height: 14px; fill: var(--teal); flex: none; }

  .card--back .brand { padding-top: 104px; gap: 20px; }
  .card--back .brand__dot { width: 34px; height: 34px; background: var(--paper); }
  .card--back .brand__name { color: var(--paper); font-size: 44px; line-height: 1; }
  .back__url {
    position: absolute; left: 0; right: 0; top: 293px;
    font-size: 16px; letter-spacing: 2.4px; color: var(--paper);
  }
</style>
</head>
<body>
  <section class="card card--front">
    <div class="brand">
      <span class="brand__dot"></span>
      <span class="brand__name">The Brightwater Compass</span>
    </div>
    <p class="holder">Corinne Fabrelle</p>
    <ul class="contacts">
      <li>
        <svg viewBox="0 0 16 16" aria-hidden="true"><path d="M3.6 1.2l2.3 2.6c.4.4.4 1 0 1.4L4.7 6.4c.9 2 2.6 3.7 4.6 4.6l1.2-1.2c.4-.4 1-.4 1.4 0l2.6 2.3c.4.4.4 1 0 1.4l-1.3 1.3C10.3 15.4 .6 5.7 1.2 2.7l1.3-1.3c.3-.4.8-.4 1.1-.2z"/></svg>
        <span>+34 612 98 70 31</span>
      </li>
      <li>
        <svg viewBox="0 0 16 16" aria-hidden="true"><path d="M1 3h14v1.2L8 8.6 1 4.2z"/><path d="M1 5.6l7 4.4 7-4.4V13H1z"/></svg>
        <span>corinne.fabrelle@thebrightwatercompass-mail.net</span>
      </li>
      <li>
        <svg viewBox="0 0 16 16" aria-hidden="true"><circle cx="8" cy="8" r="7"/><path d="M1.5 8h13M8 1c2.2 2 2.2 12 0 14M8 1c-2.2 2-2.2 12 0 14" stroke="#fff" stroke-width="1" fill="none"/></svg>
        <span>www.thebrightwatercompass-mail.net</span>
      </li>
    </ul>
  </section>

  <section class="card card--back">
    <div class="brand">
      <span class="brand__dot"></span>
      <span class="brand__name">The Brightwater Compass</span>
    </div>
    <p class="back__url">www.thebrightwatercompass-mail.net</p>
  </section>
</body>
</html>
```